Tavrel Fitness business cards

I need a business card for my company called Tavrel Fitness. I am a certified personal trainer, QMB certified, Hippo Pilates certified, and Vital paths certified. I am also an independent KORVEL rep, the number #1 rated nutritional and supplement product in the country. The card needs to convey Health, Wellness, Living Life and Loving It. I want it to be clean, sharp, eye-catching. Tantalizing.
Updates

for some reason, I'm unable to upload the pics I need. Stay tuned..

Industry/Entity Type

Business

Contact Information for Business Card

Tavrel Fitness
Mona Lykkestad, Owner
mona@tavrelfitness-example.com
555-203-4471
tavrelfitness-example.com
mona@tavrelfitness-example.com

Font styles to use
Serif

Requirements
Must have
• Must use pic of me and KORVEL logo

```html
<!DOCTYPE html>
<html lang="en">
<head>
<meta charset="utf-8">
<title>Tavrel Fitness – Business Cards</title>
<link rel="stylesheet" href="https://fonts.googleapis.com/css2?family=Cinzel:wght@600&family=Domine:wght@400;700&family=Open+Sans:wght@400;700&display=swap">
<style>
  :root {
    --page-bg: #e6e6e6;
    --royal-deep: #27379a;
    --royal-light: #4064d2;
    --charcoal: #3a3b40;
    --quote-bar: #1b1c1f;
    --quote-text: #d6d6d6;
    --brand-blue: #1b4f91;
    --band-blue: #175497;
    --rule-grey: #b3b3b3;
    --stripe-grey: #efefef;
    --ink: #222222;
    --muted: #8a8a8a;
    --white: #ffffff;
    --photo-light: #efe3c8;
    --photo-warm: #c9a67a;
  }
  * { box-sizing: border-box; margin: 0; padding: 0; }
  html, body {
    width: 1200px; height: 900px; overflow: hidden;
    background: var(--page-bg);
  }
  .canvas { position: relative; width: 1200px; height: 900px; }

  .card {
    position: absolute; left: 240px;
    width: 720px; height: 411px;
    overflow: hidden;
    box-shadow: 0 6px 18px rgba(0,0,0,0.18);
  }

  /* Photo side */
  .card--front {
    top: 26px;
    background: linear-gradient(160deg, var(--royal-deep) 0%, var(--royal-light) 100%);
  }
  .card--front .accent { position: absolute; inset: 0; }
  .portrait {
    position: absolute; left: 40px; top: 52px;
    width: 300px; height: 240px;
    border: 8px solid var(--white);
    background: radial-gradient(circle at 50% 40%, var(--photo-light) 0%, var(--photo-warm) 100%);
  }
  .front-brand {
    position: absolute; left: 400px; top: 48px; width: 290px;
    text-align: center; color: var(--white);
  }
  .front-brand .company {
    font-family: 'Cinzel', serif; font-weight: 600; font-size: 32px;
    letter-spacing: 1px;
  }
  .front-brand .person {
    font-family: 'Domine', serif; font-size: 17px; margin-top: 4px;
  }
  .cert-badge {
    position: absolute; background: var(--white);
  }
  .cert-badge--wide { left: 418px; top: 196px; width: 150px; height: 46px; }
  .cert-badge--square { left: 584px; top: 172px; width: 110px; height: 64px; }
  .quote {
    position: absolute; left: 0; right: 0; bottom: 0; height: 72px;
    background: var(--quote-bar);
    display: flex; align-items: center; justify-content: flex-end;
    padding-right: 28px;
    font-family: 'Open Sans', sans-serif; font-size: 16px; color: var(--quote-text);
  }

  /* Contact side */
  .card--back { top: 463px; background: var(--white); }
  .stripe-band {
    position: absolute; left: 0; right: 0; top: 22px; height: 118px;
    background: var(--stripe-grey);
  }
  .back-rule {
    position: absolute; left: 0; right: 0; top: 140px; height: 5px;
    background: var(--rule-grey);
  }
  .back-company {
    position: absolute; left: 38px; top: 62px;
    font-family: 'Cinzel', serif; font-weight: 600; font-size: 36px;
    color: var(--brand-blue); letter-spacing: 1px;
  }
  .back-person { position: absolute; left: 420px; top: 78px; }
  .back-person .name {
    font-family: 'Domine', serif; font-weight: 700; font-size: 20px; color: var(--ink);
  }
  .back-person .role {
    font-family: 'Domine', serif; font-size: 17px; color: var(--muted); margin-top: 2px;
  }
  .contact-list {
    position: absolute; left: 38px; top: 196px; list-style: none;
    font-family: 'Open Sans', sans-serif; font-size: 15px; color: var(--ink);
  }
  .contact-list li { display: flex; align-items: center; gap: 14px; height: 26px; }
  .contact-list svg { width: 18px; height: 16px; fill: var(--ink); }
  .partner {
    position: absolute; left: 560px; top: 230px;
    display: flex; align-items: center; gap: 10px;
  }
  .partner .mark {
    width: 14px; height: 14px; background: var(--band-blue);
  }
  .partner .label {
    font-family: 'Open Sans', sans-serif; font-weight: 400; font-size: 18px;
    color: var(--band-blue);
  }
  .blue-band {
    position: absolute; left: 0; right: 0; top: 318px; height: 44px;
    background: var(--band-blue);
  }
</style>
</head>
<body>
<main class="canvas">

  <section class="card card--front">
    <svg class="accent" viewBox="0 0 720 411" aria-hidden="true">
      <polygon points="370,262 720,240 720,339 370,339" fill="var(--charcoal)"/>
    </svg>
    <div class="portrait" role="img" aria-label="Portrait photo of Mona Lykkestad"></div>
    <div class="front-brand">
      <div class="company">Tavrel Fitness</div>
      <div class="person">Mona Lykkestad</div>
    </div>
    <div class="cert-badge cert-badge--wide" role="img" aria-label="Certification badge"></div>
    <div class="cert-badge cert-badge--square" role="img" aria-label="Certification badge"></div>
    <p class="quote">He who has health, has hope; and he who has hope, has everything.</p>
  </section>

  <section class="card card--back">
    <div class="stripe-band"></div>
    <div class="back-rule"></div>
    <div class="back-company">Tavrel Fitness</div>
    <div class="back-person">
      <div class="name">Mona Lykkestad</div>
      <div class="role">Personal Trainer</div>
    </div>
    <ul class="contact-list">
      <li>
        <svg viewBox="0 0 18 16" aria-hidden="true"><path d="M1 3h16v10H1z M1 3l8 6 8-6" fill="none" stroke="#222" stroke-width="1.6"/></svg>
        mona@tavrelfitness-example.com
      </li>
      <li>
        <svg viewBox="0 0 18 16" aria-hidden="true"><path d="M2 5c0-2 2-3 7-3s7 1 7 3v1h-4V5H6v1H2z M4 8h10l2 6H2z"/></svg>
        555-203-4471
      </li>
      <li>
        <svg viewBox="0 0 18 16" aria-hidden="true"><path d="M3 2h12v9H3z M4.5 3.5v6h9v-6z M1 12h16v2H1z"/></svg>
        www.tavrelfitness-example.com
      </li>
    </ul>
    <div class="partner">
      <span class="mark"></span>
      <span class="label">KORVEL</span>
    </div>
    <div class="blue-band"></div>
  </section>

</main>
</body>
</html>
```